Insurance Firm needs Stationary and Corporate Identity

We have a logo (provided) - we need a business card, letterhead, booklet cover, Benefit & Travel card design, and brand guide.
LRC (Larkmoor Relief Cooperative) is a National (Canadian) family-run benefits firm. We've been providing alternative benefit models to small and medium sized businesses for almost 25 years! Our goal is to create long-lasting customer relationships by partnering with our clients to become their dedicated benefits division instead of just selling a product to them.

Benefit & Travel Cards: We provide the benefit card to employees to allow them to pay for drugs at their pharmacy and dental services electronically.
The travel card is for medical emergencies while travelling outside of Canada.

Brand Guide: Once the stationary is complete, the brand guide will allow us to streamline the use of our logo's and fonts for internal and external use. We will expect that this will be a paid project for our design winner after the contest closes and we will negotiate the pricetag for this at that time.

Target Market(s)

Business Owners, Entrepreneurs, HR Professionals

Industry/Entity Type

Insurance Agency

Font styles to use
Sans Serif

Requirements
Must have
• business card, letterhead, health card, travel card, booklet cover (some current samples provided)

```html
<!DOCTYPE html>
<html lang="en">
<head>
<meta charset="utf-8">
<title>Larkmoor Relief Cooperative – Letterhead</title>
<link href="https://fonts.googleapis.com/css2?family=Lato:wght@400;700&display=swap" rel="stylesheet">
<style>
  :root {
    --backdrop: #262626;
    --paper: #ffffff;
    --paper-shade: #ededed;
    --brand-red: #e31b23;
    --panel-dark: #333333;
    --text-light: #e6e6e6;
    --logo-grey: #8f8f8f;
  }
  html, body {
    margin: 0;
    width: 960px;
    height: 1200px;
    overflow: hidden;
    background: var(--backdrop);
    font-family: "Lato", sans-serif;
  }
  .letterhead {
    position: absolute;
    left: 70px;
    top: 20px;
    width: 820px;
    height: 1160px;
    background: linear-gradient(135deg, var(--paper) 30%, var(--paper-shade) 100%);
    box-shadow: 0 6px 18px rgba(0,0,0,0.5);
    overflow: hidden;
  }
  .letterhead-shapes {
    position: absolute;
    left: 0;
    top: 0;
  }
  .contact-item {
    position: absolute;
    left: 96px;
    width: 205px;
  }
  .contact-label {
    color: var(--brand-red);
    font-size: 14px;
    line-height: 20px;
    margin: 0 0 5px;
  }
  .contact-value {
    color: var(--text-light);
    font-size: 13px;
    line-height: 25px;
    letter-spacing: 0.3px;
    margin: 0;
  }
  .contact-address { top: 337px; }
  .contact-phone   { top: 493px; }
  .contact-email   { top: 611px; }
  .contact-website { top: 733px; }
  .brand-block {
    position: absolute;
    left: 57px;
    width: 247px;
    top: 880px;
    text-align: center;
    color: var(--logo-grey);
    font-weight: 400;
  }
  .brand-initials {
    font-size: 68px;
    line-height: 72px;
    letter-spacing: 2px;
    margin: 0;
  }
  .brand-name {
    font-size: 14px;
    line-height: 19px;
    letter-spacing: 1.5px;
    text-transform: uppercase;
    margin: 6px 0 0;
  }
</style>
</head>
<body>
  <main class="letterhead">
    <svg class="letterhead-shapes" width="820" height="1160" viewBox="0 0 820 1160" aria-hidden="true">
      <polygon class="accent-band" points="0,0 51,0 51,1016 0,991" fill="var(--brand-red)"/>
      <polygon class="contact-panel" points="57,195 304,295 304,1160 57,1160" fill="var(--panel-dark)"/>

      <g class="icon icon-pin" transform="translate(54 357)">
        <circle r="22" fill="#fff" stroke="#d9d9d9" stroke-width="1"/>
        <circle r="15" fill="var(--brand-red)"/>
        <path d="M0,-8 a6,6 0 0 1 6,6 c0,4 -6,10 -6,10 c0,0 -6,-6 -6,-10 a6,6 0 0 1 6,-6z" fill="#fff"/>
        <circle cy="-2" r="2.2" fill="var(--brand-red)"/>
      </g>
      <g class="icon icon-mail" transform="translate(54 512)">
        <circle r="22" fill="#fff" stroke="#d9d9d9" stroke-width="1"/>
        <circle r="15" fill="var(--brand-red)"/>
        <rect x="-8" y="-5.5" width="16" height="11" fill="#fff"/>
        <path d="M-8,-5.5 L0,1 L8,-5.5" fill="none" stroke="var(--brand-red)" stroke-width="1.4"/>
      </g>
      <g class="icon icon-phone" transform="translate(54 631)">
        <circle r="22" fill="#fff" stroke="#d9d9d9" stroke-width="1"/>
        <circle r="15" fill="var(--brand-red)"/>
        <path d="M-4,-8 l3,0 l1,4 l-2,2 c1,3 3,5 5,6 l2,-2 l4,1 l0,3 c-8,1 -15,-6 -13,-14z" fill="#fff"/>
      </g>
      <g class="icon icon-globe" transform="translate(54 752)">
        <circle r="22" fill="#fff" stroke="#d9d9d9" stroke-width="1"/>
        <circle r="15" fill="var(--brand-red)"/>
        <g fill="none" stroke="#fff" stroke-width="1.4">
          <circle r="8"/>
          <ellipse rx="3.5" ry="8"/>
          <line x1="-8" y1="0" x2="8" y2="0"/>
          <line x1="-7" y1="-4" x2="7" y2="-4"/>
          <line x1="-7" y1="4" x2="7" y2="4"/>
        </g>
      </g>
    </svg>

    <section class="contact-item contact-address">
      <p class="contact-label">Address</p>
      <p class="contact-value">48 Harbour Road West, Suite<br>110 - Box 512, Ashgrove,<br>ON, L0B 2M0</p>
    </section>
    <section class="contact-item contact-phone">
      <p class="contact-label">Phone</p>
      <p class="contact-value">1-800-555-0148</p>
    </section>
    <section class="contact-item contact-email">
      <p class="contact-label">Email</p>
      <p class="contact-value">larkmoorrelief.com</p>
    </section>
    <section class="contact-item contact-website">
      <p class="contact-label">Website</p>
      <p class="contact-value">larkmoorrelief.com</p>
    </section>

    <div class="brand-block">
      <p class="brand-initials">LRC</p>
      <p class="brand-name">Larkmoor Relief<br>Cooperative</p>
    </div>
  </main>
</body>
</html>
```